Re design current site.

Redesign of the current site. Like current design But I don't own it so I need a custom design similar to the current one. Want the model pictures to be shown off as they currently do on the home page I want to show off contact info make it very noticeable and readable.
Target Market(s)
Males age 30-60
Number of Pages Required
1 page
Requirements
Must have
- Must show off model pictures on the page. Must show contact info easy to read easy to find.

```html
<!DOCTYPE html>
<html lang="en">
<head>
<meta charset="utf-8">
<title>Vella Models</title>
<link rel="stylesheet" href="https://fonts.googleapis.com/css2?family=Exo+2:wght@300;400&family=Open+Sans:wght@400;600&display=swap">
<style>
:root{
  --red:#e31e24;
  --panel:#1c1c20;
  --line:#2c2c31;
  --white:#ffffff;
  --text:#cfcfd3;
  --muted:#7d7d84;
  --icon:#b5b5bb;
  --head-font:"Exo 2",sans-serif;
  --body-font:"Open Sans",sans-serif;
}
*{box-sizing:border-box;margin:0;padding:0}
html,body{width:754px;height:1200px;overflow:hidden}
body{position:relative;background:radial-gradient(ellipse at 50% 20%,#3a3030 0%,#1f1d1f 55%,#141416 100%);font-family:var(--body-font);color:var(--text)}
.abs{position:absolute}
.panel{position:absolute;left:94px;top:19px;width:565px;height:1154px;background:var(--panel)}
.header{position:absolute;left:94px;top:19px;width:565px;height:95px;background:linear-gradient(90deg,#1e1c1d 0%,#2a2323 50%,#1e1c1d 100%)}
.brand{left:118px;top:52px;display:flex;align-items:center;gap:8px;font-family:var(--head-font);font-weight:300;font-size:24px;color:var(--red);letter-spacing:.5px}
.brand-mark{width:12px;height:12px;background:var(--red)}
.contact-label{font-family:var(--head-font);font-size:7.5px;color:var(--white);letter-spacing:.3px}
.contact-value{font-family:var(--head-font);font-weight:300;font-size:11.5px;color:var(--text)}
.nav{position:absolute;left:94px;top:114px;width:565px;height:36px;background:#202024}
.nav a{position:absolute;top:12px;font-family:var(--head-font);font-weight:300;font-size:10px;color:var(--text);text-decoration:none}
.social{position:absolute;width:21px;height:21px;border:1px solid #8a8a90;border-radius:50%;display:flex;align-items:center;justify-content:center}
.social svg{width:9px;height:9px;fill:none;stroke:var(--icon);stroke-width:1.4;stroke-linecap:round;stroke-linejoin:round}
.hero{position:absolute;left:94px;top:150px;width:565px;height:272px;background:radial-gradient(ellipse at 75% 45%,#b9856a 0%,#7a4636 35%,#3c1e19 75%,#241413 100%)}
.hero-figure{position:absolute;left:0;top:10px;width:240px;height:262px;background:radial-gradient(ellipse at 45% 60%,#a3141a 0%,#6d0e12 55%,rgba(60,20,20,0) 80%)}
.hero-title{position:absolute;left:330px;top:82px;width:125px;height:28px;background:var(--red);color:var(--white);font-family:var(--head-font);font-size:15px;line-height:28px;text-align:center}
.hero-sub{position:absolute;left:330px;top:112px;width:160px;height:28px;background:rgba(40,34,36,.85);color:var(--white);font-family:var(--body-font);font-size:14px;line-height:28px;padding-left:10px}
.hero-sub svg{position:absolute;right:8px;top:7px}
.dots{position:absolute;left:248px;top:245px;display:flex;gap:4px}
.dots span{width:22px;height:2px;background:var(--white)}
.dots span.on{background:var(--red)}
.feature{position:absolute;top:450px;width:170px;text-align:center}
.feature-icon{width:77px;height:77px;border-radius:50%;background:var(--red);margin:0 auto;display:flex;align-items:center;justify-content:center}
.feature-icon svg{fill:none;stroke:var(--white);stroke-width:3;stroke-linecap:round;stroke-linejoin:round}
.feature h3{font-family:var(--head-font);font-weight:300;font-size:16px;color:var(--white);margin-top:9px}
.feature p{font-size:7.4px;line-height:11.2px;color:var(--muted);margin-top:6px;padding:0 12px}
.rule{position:absolute;left:94px;top:634px;width:565px;height:1px;background:var(--line)}
.vrule{position:absolute;width:1px;background:var(--line)}
.section-title{position:absolute;font-family:var(--head-font);font-weight:300;font-size:16px;color:var(--white)}
.section-title::after{content:"";position:absolute;left:0;top:24px;width:36px;height:2px;background:var(--red)}
.lead{left:125px;top:692px;width:180px;font-size:8.4px;line-height:13px;color:var(--white)}
.body-copy{font-size:7.6px;line-height:13.4px;color:var(--muted)}
.btn{position:absolute;background:var(--red);color:var(--white);font-family:var(--head-font);font-size:8px;text-align:center}
.model{position:absolute;width:88px;height:66px}
.model-card{background:var(--red);padding:8px 0 0 7px;color:var(--white)}
.model-card h4{font-family:var(--head-font);font-weight:400;font-size:11px;text-align:center;margin-bottom:4px}
.model-card p{font-size:6.2px;line-height:12px}
.ad-label{left:0;width:754px;top:893px;text-align:center;font-family:serif;font-size:6.5px;color:var(--white)}
.links a{position:absolute;left:350px;font-size:7px;color:var(--text);text-decoration:none;padding-left:10px}
.links a::before{content:"";position:absolute;left:0;top:4px;width:7px;height:1px;background:var(--red)}
.touch-label{font-family:var(--head-font);font-size:9px;color:var(--red)}
.touch-value{font-family:var(--head-font);font-weight:300;font-size:13.5px;color:var(--text)}
.email-input{left:125px;top:1086px;width:162px;height:26px;background:#0f0f11;font-size:7px;color:var(--muted);padding:8px 8px}
.footer{position:absolute;left:94px;top:1173px;width:565px;height:27px;background:var(--red);color:var(--white);font-size:7px;text-align:center;line-height:27px}
</style>
</head>
<body>
<svg width="0" height="0" style="position:absolute">
  <defs>
    <g id="ic-share"><circle cx="3" cy="8" r="2"/><circle cx="13" cy="3" r="2"/><circle cx="13" cy="13" r="2"/><path d="M5 7l6-3M5 9l6 3"/></g>
    <g id="ic-chat"><path d="M2 3h12v8H7l-3 3v-3H2z"/></g>
    <g id="ic-link"><path d="M7 9l2-2M6 6l-2 2a2.5 2.5 0 003.5 3.5l1-1M10 10l2-2A2.5 2.5 0 008.5 4.5l-1 1"/></g>
    <g id="ic-mail"><rect x="2" y="4" width="12" height="9"/><path d="M2 4l6 5 6-5"/></g>
  </defs>
</svg>

<div class="panel"></div>
<header class="header"></header>
<div class="abs brand"><span class="brand-mark"></span>VELLA MODELS</div>

<svg class="abs" style="left:462px;top:42px" width="16" height="16" viewBox="0 0 16 16"><path d="M3 1.5l3 3-1.6 1.8c1 2 2.4 3.5 4.4 4.5L10.6 9l3 3-2 2C6.5 13.5 2.5 9.5 1.5 3.5z" fill="none" stroke="#e31e24" stroke-width="1.2"/></svg>
<div class="abs contact-label" style="left:484px;top:36px">CALL US TODAY</div>
<div class="abs contact-value" style="left:484px;top:46px">5550142871</div>
<svg class="abs" style="left:461px;top:78px" width="18" height="15" viewBox="0 0 18 15"><rect x="1" y="3" width="16" height="11" fill="none" stroke="#e31e24" stroke-width="1.2"/><path d="M1 3l8 6 8-6" fill="none" stroke="#e31e24" stroke-width="1.2"/></svg>
<div class="abs contact-label" style="left:484px;top:77px">EMAIL US</div>
<div class="abs contact-value" style="left:484px;top:84px">hello@vellamodels.com</div>

<nav class="nav">
  <a style="left:20px">HOME</a><a style="left:80px">BOOKINGS</a><a style="left:160px">RATES</a><a style="left:202px">MODELS</a><a style="left:258px">EMPLOYMENT</a><a style="left:352px">LINKS</a>
  <span class="social" style="left:432px;top:7px"><svg viewBox="0 0 16 16"><use href="#ic-share"/></svg></span>
  <span class="social" style="left:464px;top:7px"><svg viewBox="0 0 16 16"><use href="#ic-chat"/></svg></span>
  <span class="social" style="left:497px;top:7px"><svg viewBox="0 0 16 16"><use href="#ic-link"/></svg></span>
  <span class="social" style="left:530px;top:7px"><svg viewBox="0 0 16 16"><use href="#ic-mail"/></svg></span>
</nav>

<section class="hero">
  <div class="hero-figure" role="img" aria-label="Model in a flowing red satin gown against a copper hexagon wall"></div>
  <div class="hero-title">VELLA MODELS</div>
  <div class="hero-sub">Concierge Service<svg width="16" height="14" viewBox="0 0 16 14"><path d="M1 6c3 0 7 0 10 0M8 2l5 4-5 4M3 10l3 2" fill="none" stroke="#fff" stroke-width="1.2"/></svg></div>
  <div class="dots"><span class="on"></span><span></span><span></span></div>
</section>

<div class="feature" style="left:111px">
  <div class="feature-icon"><svg width="40" height="40" viewBox="0 0 40 40" style="stroke-width:2.4"><path d="M20 3l5 12h13l-10.5 8 4 13L20 28 8.5 36l4-13L2 15h13z"/></svg></div>
  <h3>TOP MODLES</h3>
  <p>Ane nulla eram lorem. Summis quo sed legam probant, ab cillum dolor nulla doctrina. Iis dolore officia. Ita ita varias quibusdam, hic offendit.</p>
</div>
<div class="feature" style="left:292px">
  <div class="feature-icon"><svg width="40" height="44" viewBox="0 0 40 44"><circle cx="20" cy="15" r="11"/><path d="M20 26v15M13 35h14"/></svg></div>
  <h3>WOMEN MODLES</h3>
  <p>Ane nulla eram lorem. Summis quo sed legam probant, ab cillum dolor nulla doctrina. Iis dolore officia. Ita ita varias quibusdam, hic offendit.</p>
</div>
<div class="feature" style="left:473px">
  <div class="feature-icon"><svg width="42" height="42" viewBox="0 0 42 42"><circle cx="17" cy="25" r="11"/><path d="M25 17L36 6M26 6h10v10"/></svg></div>
  <h3>MEN MODLES</h3>
  <p>Ane nulla eram lorem. Summis quo sed legam probant, ab cillum dolor nulla doctrina. Iis dolore officia. Ita ita varias quibusdam, hic offendit.</p>
</div>

<div class="rule"></div>

<h2 class="section-title" style="left:125px;top:660px">ABOUT US</h2>
<p class="abs lead">Male &amp; female couple available as well.<br>Custom clips and videos available for sale!</p>
<p class="abs body-copy" style="left:125px;top:726px;width:172px">VellaModels Concierge Service allows clients to request VellaModels to search for models in the location you plan on traveling to. We will search and find attractive models for the dates requested. We also verify they are interested in the service you expect/request and that the pictures we have are recent and real.</p>
<div class="btn" style="left:125px;top:836px;width:66px;height:20px;line-height:20px">READ MORE</div>

<div class="vrule" style="left:321px;top:664px;height:208px"></div>

<h2 class="section-title" style="left:349px;top:660px">OUR MODELS</h2>
<div class="model model-card" style="left:349px;top:695px"><h4>Sienna</h4><p>Age: 23<br>Height: 5'0<br>Weight: 110</p></div>
<div class="model" style="left:445px;top:695px;background:linear-gradient(135deg,#7a93b8,#e8e2dc 60%,#c9a07c)" role="img" aria-label="Model photo lying on white sheets"></div>
<div class="model" style="left:540px;top:695px;background:linear-gradient(135deg,#2a3140,#7a1a22 60%,#c02028)" role="img" aria-label="Model photo in red dress"></div>
<div class="model" style="left:349px;top:769px;background:linear-gradient(135deg,#d9d9dc,#5a5a60 60%,#e6e6e8)" role="img" aria-label="Model photo in grey jacket"></div>
<div class="model" style="left:445px;top:769px;background:linear-gradient(135deg,#2a2220,#8a6450 60%,#1a1514)" role="img" aria-label="Model photo in low light"></div>
<div class="model" style="left:540px;top:769px;background:linear-gradient(135deg,#c9d4dc,#d4a48a 55%,#b92a2e)" role="img" aria-label="Model photo in polka dot outfit"></div>
<div class="btn" style="left:449px;top:853px;width:82px;height:20px;line-height:20px">VIEW ALL MODELS</div>

<div class="abs ad-label">Ads by AdNetwork Co.</div>
<div class="abs" style="left:126px;top:906px;width:238px;height:70px;background:linear-gradient(90deg,#d8b6a4,#f2f2f2 60%,#ffffff)" role="img" aria-label="Sponsor banner advertisement"></div>
<div class="abs" style="left:364px;top:906px;width:265px;height:70px;background:linear-gradient(90deg,#6a5048,#3a2a28 60%,#1f1a1a)" role="img" aria-label="Sponsor banner advertisement"></div>

<h2 class="section-title" style="left:125px;top:1004px">JOIN MY NEWSLETTER</h2>
<p class="abs body-copy" style="left:125px;top:1037px;width:164px">Voluptate illum dolore ita ipsum, quid labore deserunt singulis, labore admodu multos malis ea nam nam tamen fore</p>
<div class="abs email-input">Enter Your Email ID</div>
<div class="btn" style="left:125px;top:1124px;width:66px;height:21px;line-height:21px">JOIN NOW!</div>

<div class="vrule" style="left:321px;top:1000px;height:156px"></div>

<h2 class="section-title" style="left:350px;top:1004px">GET IN TOUCH</h2>
<div class="links">
  <a style="top:1037px">HOME</a><a style="top:1056px">BOOKINGS</a><a style="top:1076px">RATES</a><a style="top:1095px">MODELS</a><a style="top:1115px">EMPLOYMENT</a><a style="top:1134px">LINKS</a>
</div>
<div class="abs touch-label" style="left:455px;top:1036px">CALL US TODAY</div>
<div class="abs touch-value" style="left:455px;top:1046px">5550142871</div>
<div class="abs touch-label" style="left:455px;top:1074px">EMAIL US</div>
<div class="abs touch-value" style="left:455px;top:1084px">hello@vellamodels.com</div>
<div class="abs touch-label" style="left:455px;top:1113px">FOLLOW US</div>
<span class="social" style="left:454px;top:1129px"><svg viewBox="0 0 16 16"><use href="#ic-share"/></svg></span>
<span class="social" style="left:486px;top:1129px"><svg viewBox="0 0 16 16"><use href="#ic-chat"/></svg></span>
<span class="social" style="left:518px;top:1129px"><svg viewBox="0 0 16 16"><use href="#ic-link"/></svg></span>
<span class="social" style="left:551px;top:1129px"><svg viewBox="0 0 16 16"><use href="#ic-mail"/></svg></span>

<footer class="footer">Copyright © 2017 VELLA MODELS. All Rights Reserved.</footer>
</body>
</html>
```